Promotional Postcard for Mountain Bike Stunt Show

PLEASE DOWNLOAD ATTACHED ZIP FILE

This will be on a larger postcard size: 4ā€ x 9ā€ - front and back will be completely covered in text and pictures. I’m going to mail it out in envelopes.

Overview: This is promotional postcard for my mountain bike stunt show. It will be filled with text and pictures to attract clients into booking my show. It must look clean and professional. Remember: This is an action stunt show based out of the mountain states region so it must look exciting, rugged, clean and professional :)
Updates

A few additional notes: I'd also like to see the logo picture 1 used on the front to display the name of my show but then fade out to the right into whatever else you want to fit. As far as all of the text, try to put that in "dead space" in the pictures if there open air or in Picture 3 where theres an opportunity to fade out the unwanted trailer and grass showing and put text in there "action packed etc etc"

Target Market(s)

Trade shows, fairs, schools, festivals, agricultural fairs, corporate events

Industry/Entity Type

Entertainment Industry

Colors

Designer to choose colors to be used in the design.

Requirements
Must have
• FOLLOW INSTRUCTIONS IN MY ATTACHED ZIP FILE
Nice to have
• I think I'd like a dark theme/layout to the card :)

```html
<!DOCTYPE html>
<html lang="en">
<head>
<meta charset="utf-8">
<title>Stunt Show Postcard</title>
<link href="https://fonts.googleapis.com/css2?family=Alfa+Slab+One&family=Arvo:wght@700&family=Roboto:wght@500&family=Roboto+Slab:wght@600&family=Montserrat:wght@600&display=swap" rel="stylesheet">
<style>
  :root {
    --stage: #3b2a20;
    --card: #ffffff;
    --ink: #111111;
    --red: #e0241b;
    --caption-red: #a5121b;
    --caption-red-dark: #7d0c13;
    --sky-top: #2e98e6;
    --sky-low: #7fcbf5;
    --tent-white: #e9eef2;
    --barn-red: #b5312c;
    --field-green: #4c7a36;
    --crowd: #5e4336;
    --bubble-fill: #8fd0f7;
  }
  * { margin: 0; padding: 0; box-sizing: border-box; }
  html, body { width: 1200px; height: 903px; overflow: hidden; }
  body { background: var(--stage); position: relative; }

  .postcard {
    position: absolute; left: 31px; top: 199px;
    width: 1137px; height: 505px;
    background: var(--card);
  }
  .hero-photo {
    position: absolute; left: 25px; top: 25px; width: 836px; height: 455px;
    clip-path: polygon(0 0, 772px 0, 836px 455px, 0 455px);
    background: linear-gradient(180deg,
      var(--sky-top) 0%, var(--sky-low) 58%,
      var(--tent-white) 64%, var(--barn-red) 70%,
      var(--field-green) 76%, var(--crowd) 86%, #4a352b 100%);
  }
  .headline {
    position: absolute; left: 47px; font-family: "Alfa Slab One", serif;
    font-size: 36px; line-height: 1; letter-spacing: 0.6px; white-space: nowrap;
  }
  .headline--black { top: 45px; color: var(--ink); }
  .headline--red { top: 97px; color: var(--red); }
  .tagline {
    position: absolute; left: 47px; top: 151px;
    font-family: "Roboto", sans-serif; font-weight: 500; font-size: 29px; color: var(--ink);
  }
  .speech-bubble { position: absolute; left: 600px; top: 103px; width: 190px; height: 165px; }
  .speech-text {
    position: absolute; left: 603px; top: 114px; width: 182px; text-align: center;
    font-family: "Roboto Slab", "Arvo", serif; font-weight: 600; font-size: 23px; line-height: 31px; color: var(--red);
  }
  .side-photo { position: absolute; overflow: hidden; }
  .side-photo--crowd {
    left: 805px; top: 25px; width: 307px; height: 143px;
    clip-path: polygon(0 0, 307px 0, 307px 143px, 20px 143px);
    background: linear-gradient(180deg, #3d9fe5 0%, #86c6ea 38%, #5a8a44 55%, #3f5f30 100%);
  }
  .side-photo--autograph {
    left: 825px; top: 174px; width: 287px; height: 155px;
    clip-path: polygon(0 0, 287px 0, 287px 155px, 22px 155px);
    background: linear-gradient(90deg, #e4e6e8 0%, #e4e6e8 35%, #f2f4f6 60%, #5e8a44 100%);
  }
  .side-photo--giveaway {
    left: 850px; top: 338px; width: 262px; height: 142px;
    clip-path: polygon(0 0, 262px 0, 262px 142px, 20px 142px);
    background: linear-gradient(180deg, #56663c 0%, #6b6f5a 35%, #d9d6d8 60%, #6a5a4c 100%);
  }
  .caption {
    position: absolute; left: 0; right: 0; bottom: 0; height: 24px;
    background: linear-gradient(90deg, var(--caption-red-dark), var(--caption-red) 50%, var(--caption-red-dark));
    color: #fff; font-family: "Montserrat", sans-serif; font-weight: 600; font-size: 13.5px;
    line-height: 24px; text-align: center; padding-left: 20px; white-space: nowrap;
  }
</style>
</head>
<body>
  <div class="postcard">
    <div class="hero-photo" role="img" aria-label="Rider balancing a trials bike mid-air above ramps in front of a large fair crowd, red barns and white tents under a blue sky"></div>

    <div class="headline headline--black">AWESOME ENTERTAINMENT</div>
    <div class="headline headline--red">FOR YOUR EVENT!</div>
    <div class="tagline">THIS SHOW DELIVERS!</div>

    <svg class="speech-bubble" viewBox="0 0 190 165" aria-hidden="true">
      <path d="M14 4 H176 Q186 4 186 14 V108 Q186 118 176 118 H62 L30 157 L38 118 H14 Q4 118 4 108 V14 Q4 4 14 4 Z"
            fill="var(--bubble-fill)" fill-opacity="0.55" stroke="#ffffff" stroke-width="5" stroke-linejoin="round"/>
    </svg>
    <div class="speech-text">Loads of<br>high-energy<br>action!</div>

    <div class="side-photo side-photo--crowd" role="img" aria-label="Performer giving a high five to a child volunteer beside the show trailer, crowd seated on the grass">
      <div class="caption">Audience Engagement!</div>
    </div>
    <div class="side-photo side-photo--autograph" role="img" aria-label="Rider in a helmet signing autographs for children at a table">
      <div class="caption">Meet n' greet autograph session</div>
    </div>
    <div class="side-photo side-photo--giveaway" role="img" aria-label="Wrapped bags of free giveaway items on a table">
      <div class="caption">Free giveaways!</div>
    </div>
  </div>
</body>
</html>
```